Blogging Platform for Christian Missions

We need the main (one) page design for FaithPostly. FaithPostly is a blogging platform for people (missionaries) who work for Christian Mission organisations in various countries. It will provides an easy way for them to setup and maintain a blog that will have features specifically for missions.

There's a lot of work involved in creating a web page design so I am happy to receive many quick rough designs. I will select my favourite four or five designs and these can submit the full design.

Please see the attached wireframe. Please also see the attached logo.

Main colours
- black
- white
- grey
- red (see logo colour) can be used occasionally eg. titles
- another complementary colour - occasionally used

Photos uploaded by the missionaries will provide colour for the website.

It needs to be a clean design that is not cluttered. The main focus are the blog posts. The information on the side complements the blog. There are navigational options at the top and bottom. The FaithPostly logo is not the main focus. The person's name (blog owner) is what needs to be most prominent.

I love the BrightNoma design (http://www.brightnoma-demo.net/). I particularly like the soft design - light grey background, white background boxes for content. The focus is the content - text and photos. I also like the subtle use of breakout image - "Step into the Venture". I like the black navigation header and the black footer. I do not want a exact copy of the site but I'd like to use this concept .

I also like this Quibbly design (http://calm.quibbly-demo.net/theme/preview/5193) because of the white box (and the shadow) for the content. I also like how the word "Quote" and the number of "notes" breaks out of the white content area (see attachment). I'd like to do this, if possible with the date. This is just a "nice to have" - definitely not essential. I don't like the font for the title in this example.

We have build a simple prototype already. I cautiously show this because I want the the design of this to be completely ignored. I used a free template. Along with the wireframe this prototype should an idea of what kind of content will be displayed but please don't look too much at it.
http://faithpostly-demo.org/blog/1

The design will be used to create a website using Verdant. We will use zScript so feel free to suggest an animation or lightbox effect to make your design more dynamic. This is a nice to have.

Once we have our final design we will need to define the style for:
- h1 through h4 tags
- Paragraphs
- Lists
- Block quotes
- Italics, bolding and underlining
- Links, including active, hover and visited states

Please let me know what additional information you need. Also let me know if there is something I have not considered.

Target Market(s)

The target customers are mission workers aged 25-35 who will post blog entries. These posts will be read by their friends and family.

Requirements
Must have
• Clean simple design. Must be inspired by the BrightNoma (http://www.brightnoma-demo.net/) design without copying it.
Nice to have
• Design element that breaks out of the boxes. See the screenshot attached from the Quibbly site. Described more in the project overview.
Should not have
• Should not use fonts that are not web-friendly. Should not have features that will be difficult to implement using HTML/CSS.

```html
<!DOCTYPE html>
<html lang="en">
<head>
<meta charset="utf-8">
<title>Clara Dunn – FaithPostly</title>
<link href="https://fonts.googleapis.com/css2?family=Open+Sans:wght@400;600;700&family=Noto+Sans:wght@400;700&family=Arimo&family=Roboto+Condensed:wght@400&display=swap" rel="stylesheet">
<style>
:root{
  --page:#ececec;
  --white:#fff;
  --ink:#2e2e2e;
  --text:#3a3a3a;
  --muted:#7a7a7a;
  --red:#b3131c;
  --red-bright:#e3202a;
  --link:#2a6fb5;
  --frame:#a9a9a9;
  --foot-a:#3b3b3b;
  --foot-b:#1f1f1f;
}
*{margin:0;padding:0;box-sizing:border-box}
html,body{width:1029px;height:1200px;overflow:hidden}
body{position:relative;background:var(--page);font-family:"Noto Sans",sans-serif;color:var(--text)}
.abs{position:absolute}
a{color:var(--link);text-decoration:underline}

.topbar{left:0;top:0;width:1029px;height:33px;background:linear-gradient(#3a3a3a,#111)}
.nav-item{top:10px;font:600 11.5px "Open Sans",sans-serif;color:#eee}
.acct-item{top:10px;font:400 10.5px "Open Sans",sans-serif;color:#ddd}

.header{left:0;top:33px;width:1029px;height:94px;background:linear-gradient(#fff 40%,#e9e9e9);border-bottom:1px solid #d8d8d8}
.brand{left:101px;top:62px;display:flex;align-items:center;gap:8px}
.brand-dot{width:34px;height:34px;border-radius:50%;background:var(--red-bright)}
.brand-name{font:600 30px "Open Sans",sans-serif;color:#555;letter-spacing:-.5px}
.search{left:693px;top:47px;width:188px;height:23px;border:1px solid #c9c9c9;border-radius:12px;background:#fff;font:400 9.5px "Open Sans",sans-serif;color:#888;padding:4px 7px}
.search-btn{left:858px;top:47px;width:24px;height:24px;border-radius:50%;background:radial-gradient(#9aa,#556)}

.owner-name{left:113px;top:160px;font:400 23px "Open Sans",sans-serif;color:var(--red)}
.owner-org{left:113px;top:190px;font:600 13px "Open Sans",sans-serif;color:#555;letter-spacing:.3px}
.follow{left:709px;top:150px;width:221px;height:42px;border-radius:7px;background:linear-gradient(#f0404a,#c5101a);color:#fff;font:600 17px "Open Sans",sans-serif;padding:10px 0 0 68px}
.follow-avatar{left:722px;top:134px;width:48px;height:56px;border-radius:8px;background:#d6d6d6;border:2px solid #fff}

.feed{left:95px;top:226px;width:599px;height:787px;background:var(--white);box-shadow:0 0 4px rgba(0,0,0,.15)}
.post-title{font:600 19px "Open Sans",sans-serif;color:var(--ink);letter-spacing:.3px}
.post-date{font:400 13.5px "Open Sans",sans-serif;color:var(--muted);letter-spacing:.3px}
.share{width:24px;height:24px;border-radius:4px}
.share.one{background:linear-gradient(#4f7fcf,#284f9a)}
.share.two{background:linear-gradient(#8fd6f3,#36a3d8)}
.copy{font-size:10.3px;line-height:15.4px;color:var(--text)}
.links{font-size:10.5px}
.links a{margin-right:12px}
.photo{left:108px;top:468px;width:317px;height:225px;background:var(--frame);padding:7px}
.photo div{width:100%;height:100%;background:linear-gradient(#4a4f86 0%,#8b86a8 40%,#c7c2c6 55%,#6f6a63 62%,#2f4a1f 78%,#1f3213)}
.pull{left:440px;top:472px;width:235px;font:400 22px/24px "Arimo",sans-serif;color:#555}

.pg{position:absolute;top:980px;height:23px;font:400 14.5px/23px "Open Sans",sans-serif;text-align:center}
.pg.num{width:26px;background:#e4e4e4;border:1px solid #c9c9c9;color:#333}
.pg.now{background:var(--red);border-color:var(--red);color:#fff}
.pg.step{width:62px;border-radius:5px;background:linear-gradient(#444,#111);color:#fff;font-size:12.5px}

.card{left:708px;width:223px;background:var(--white);border-radius:14px;box-shadow:0 0 4px rgba(0,0,0,.18)}
.card-title{font:400 15.5px "Open Sans",sans-serif;color:#444;letter-spacing:.3px}
.card-copy{font-size:9.3px;line-height:13.8px;color:#333}
.more{font-size:9.3px;color:#8a1a1a;letter-spacing:.4px}
.portrait{left:718px;top:313px;width:151px;height:122px;border:1px solid #ccc;background:#eee;padding:7px}
.portrait div{width:100%;height:100%;background:linear-gradient(135deg,#3a2a1a,#c9a064 50%,#3a2a1a)}
.map{left:725px;top:671px;width:157px;height:90px;background:#aaa;padding:5px}
.map div{width:100%;height:100%;background:linear-gradient(#e9e9e9,#cfcfcf)}
.list{list-style:none;font-size:9.3px;line-height:14.6px;color:#222}
.list li{position:relative;padding-left:12px}
.list li::before{content:"";position:absolute;left:0;top:5px;width:5px;height:5px;border-radius:50%;background:var(--red)}

.footer{left:0;top:1033px;width:1029px;height:167px;background:linear-gradient(var(--foot-a),var(--foot-b))}
.foot-head{font:400 15.5px "Roboto Condensed",sans-serif;color:#fff;display:flex;align-items:center;gap:9px;top:1046px}
.foot-head span{width:22px;height:22px;border-radius:50%;border:2px solid #888}
.foot-list{list-style:none;font:400 11px "Open Sans",sans-serif;line-height:18.9px;color:#e8e8e8;top:1076px}
.foot-list li{position:relative;padding-left:17px}
.foot-list li::before{content:"";position:absolute;left:0;top:7px;width:5px;height:5px;border-radius:50%;background:var(--red-bright)}
.foot-mark{left:625px;top:1140px;display:flex;align-items:center;gap:8px;opacity:.35}
.foot-mark span{width:40px;height:40px;border-radius:50%;background:#777}
.foot-mark b{font:600 29px "Open Sans",sans-serif;color:#777}
</style>
</head>
<body>

<div class="abs topbar"></div>
<nav>
  <span class="abs nav-item" style="left:111px">Challenges</span>
  <span class="abs nav-item" style="left:203px">Field notes</span>
  <span class="abs nav-item" style="left:293px">Community</span>
  <span class="abs nav-item" style="left:391px">About us</span>
  <span class="abs acct-item" style="left:821px">Sing in</span>
  <span class="abs acct-item" style="left:869px;top:9px">|</span>
  <span class="abs acct-item" style="left:888px">Register</span>
</nav>

<header class="abs header"></header>
<div class="abs brand"><div class="brand-dot"></div><div class="brand-name">faithpostly.org</div></div>
<div class="abs search">Advanced Search</div>
<div class="abs search-btn"></div>

<h1 class="abs owner-name">Clara Dunn</h1>
<div class="abs owner-org">Tova Australia</div>
<div class="abs follow">Follow Clara »</div>
<div class="abs follow-avatar" role="img" aria-label="Follower avatar placeholder"></div>

<main class="abs feed"></main>

<h2 class="abs post-title" style="left:105px;top:236px">Just Arrived</h2>
<div class="abs post-date" style="left:105px;top:258px">14 April 2011</div>
<div class="abs share one" style="left:605px;top:244px"></div>
<div class="abs share two" style="left:637px;top:244px"></div>
<p class="abs copy" style="left:105px;top:297px;width:568px">Lorem Ipsum is simply dummy text of the printing and typesetting industry. Lorem Ipsum has been the industry's standard dummy text ever since the 1500s, when an unknown printer took a galley of type and scrambled it to make a type specimen book.</p>
<p class="abs copy" style="left:105px;top:358px;width:578px">It has survived not only five centuries, but also the leap into electronic typesetting, remaining essentially unchanged. It was popularised in the 1960s with the release of Lettrix sheets containing Lorem Ipsum passages, and more recently with desktop publishing software like Pagewright including<br>versions of Lorem Ipsum.</p>
<div class="abs links" style="left:110px;top:439px"><a href="#">Add new comment</a> <a href="#">Read more</a></div>

<div class="abs photo"><div role="img" aria-label="Photo of a modern single-storey house at dusk with a green lawn"></div></div>
<p class="abs pull">Lorem Ipsum is simply dummy text of the printing and typesetting industry. Lorem Ipsum has been the industry's standard dummy text ever since the 1500s,</p>
<div class="abs links" style="left:108px;top:705px"><a href="#">Add new comment</a> <a href="#">Read more</a></div>

<h2 class="abs post-title" style="left:112px;top:736px">Only 14 days to go before I fly for malawi</h2>
<div class="abs post-date" style="left:112px;top:758px">30 March 2011</div>
<div class="abs share one" style="left:616px;top:731px"></div>
<div class="abs share two" style="left:648px;top:731px"></div>
<p class="abs copy" style="left:110px;top:781px;width:530px">Lorem Ipsum is simply dummy text of the printing and typesetting industry. Lorem Ipsum has been the industry's standard dummy text ever since the 1500s, when an unknown printer took a galley of type and scrambled it to make a type specimen book.</p>
<p class="abs copy" style="left:110px;top:843px;width:530px">It has survived not only five centuries, but also the leap into electronic typesetting, remaining essentially unchanged. It was popularised in the 1960s with the release of Lettrix sheets containing Lorem Ipsum passages, and more recently with desktop publishing software like Pagewright including versions of Lorem Ipsum.</p>
<div class="abs links" style="left:110px;top:910px"><a href="#">Add new comment</a> <a href="#">Read more</a></div>

<div class="pg step" style="left:194px">Previous</div>
<div class="pg num" style="left:266px">1</div>
<div class="pg num" style="left:305px">2</div>
<div class="pg num" style="left:342px">3</div>
<div class="pg num now" style="left:380px">4</div>
<div class="pg num" style="left:418px">5</div>
<div class="pg num" style="left:455px">6</div>
<div class="pg num" style="left:495px">7</div>
<div class="pg step" style="left:534px">Next</div>

<aside>
  <div class="abs card" style="top:226px;height:238px"></div>
  <h3 class="abs card-title" style="left:726px;top:232px">About Clara</h3>
  <p class="abs card-copy" style="left:719px;top:261px;width:200px;text-align:justify">Lorem Ipsum is simply dummy text of the printing and typesetting industry. Lorem Ipsum has been the industry's</p>
  <div class="abs portrait"><div role="img" aria-label="Portrait photo of the blog owner"></div></div>
  <div class="abs more" style="left:864px;top:443px">Readmore...</div>

  <div class="abs card" style="top:485px;height:139px"></div>
  <h3 class="abs card-title" style="left:725px;top:492px">About Clara Ministry</h3>
  <p class="abs card-copy" style="left:722px;top:520px;width:200px;line-height:15.4px"><b>Lorem Ipsum is simply dummy text of the printing and</b> typesetting industry. Lorem Ipsum has been the industry's standard dummy text ever since the 1500s, when an unknown printer</p>
  <div class="abs more" style="left:866px;top:604px">Readmore...</div>

  <div class="abs card" style="top:640px;height:373px"></div>
  <h3 class="abs card-title" style="left:730px;top:645px;font-size:17px">About Malwai</h3>
  <div class="abs map"><div role="img" aria-label="World map highlighting Malawi"></div></div>
  <p class="abs card-copy" style="left:729px;top:768px;width:190px;line-height:14.5px">Lorem Ipsum is simply dummy text of the printing and typesetting industry. Lorem Ipsum has been the industry</p>
  <div class="abs more" style="left:863px;top:818px">Readmore...</div>
  <h3 class="abs card-title" style="left:724px;top:841px">Tova Events</h3>
  <ul class="abs list" style="left:723px;top:865px">
    <li>Tova Prayer Event- may 15th</li>
    <li>Tova Conference - June 30th</li>
  </ul>
  <div class="abs more" style="left:859px;top:899px">Readmore...</div>
  <h3 class="abs card-title" style="left:720px;top:915px;font-size:13px">Tova Opportunitices in malawai</h3>
  <ul class="abs list" style="left:722px;top:936px">
    <li>Teacher in Blanta (2yrs)</li>
    <li>Financial Controller (long term)</li>
    <li>Project Manager (6 MOnth+)</li>
    <li>Bible College Lecturer (long term)</li>
  </ul>
  <div class="abs more" style="left:864px;top:998px">Readmore...</div>
</aside>

<footer class="abs footer"></footer>
<div class="abs foot-head" style="left:99px"><span></span>ABOUT US</div>
<div class="abs foot-head" style="left:260px"><span></span>REGIONS</div>
<div class="abs foot-head" style="left:418px"><span></span>MISSION AGENCIES</div>
<ul class="abs foot-list" style="left:104px">
  <li>About FaithPostly</li><li>Missonaris</li><li>Mission Agencies</li><li>Churhes</li><li>Mission Sippotters</li><li>Privacy</li>
</ul>
<ul class="abs foot-list" style="left:274px">
  <li>Africa</li><li>Asia</li><li>North America</li><li>Latin America</li><li>Aust pacific</li><li>Privacy</li>
</ul>
<ul class="abs foot-list" style="left:433px">
  <li>NMA</li><li>Open Horizon</li><li>Tova Australia</li><li>KLS</li>
</ul>
<div class="abs foot-mark"><span></span><b>faithpostly.org</b></div>

</body>
</html>
```